Your complete Gardening and lawn maintenance, Horticultural care. (to be on card)
We are looking at using a logo of a tree, with a recycling emblem circling the tree. The colors of choice, are burnt oranges and olive greens. Presented; simple to the eye, yet catchy to the clients in a eco-friendly way. We have uploaded a design for you to look at just to give a rough idea, you can use that or create your own ideas or play around with a mixture.

Target Market(s)

Home owners, businesses, real estates.

Industry/Entity Type

Recycling

Contact Information for Business Card

Name: Colin Breversted
Phone: 0438159027
Email: brightmossyards@mailbarn.net

Logo Text

Bright-Moss Yards

Logo styles of interest
Emblem Logo
Pictorial/Combination Logo
Abstract Logo
Requirements
Must have
• Business name: Bright-Moss Yards
and slogan : Your complete Gardening and lawn maintenance, Horticultural care

```html
<!DOCTYPE html>
<html lang="en">
<head>
<meta charset="utf-8">
<title>Bright-Moss Yards – Business Card</title>
<link rel="stylesheet" href="https://fonts.googleapis.com/css2?family=Oswald:wght@600&family=Titillium+Web:wght@300;400&display=swap">
<style>
  :root {
    --page: #ffffff;
    --card: #ffffff;
    --card-edge: #4a4a4a;
    --olive: #9a9a5c;
    --burnt-orange: #cf5400;
    --ink-light: #ffffff;
  }
  html, body {
    margin: 0;
    padding: 0;
    width: 1200px;
    height: 741px;
    overflow: hidden;
    background: var(--page);
  }
  .canvas {
    position: relative;
    width: 1200px;
    height: 741px;
  }
  .card-art {
    position: absolute;
    inset: 0;
    width: 1200px;
    height: 741px;
  }
  .brand-mark {
    position: absolute;
    left: 118px;
    top: 138px;
    width: 200px;
    height: 200px;
    border-radius: 50%;
    background: var(--olive);
  }
  .brand-name {
    position: absolute;
    left: 382px;
    top: 150px;
    margin: 0;
    font-family: "Oswald", sans-serif;
    font-weight: 600;
    font-size: 66px;
    line-height: 1;
    letter-spacing: 2px;
    color: var(--olive);
    white-space: nowrap;
  }
  .tagline {
    position: absolute;
    left: 383px;
    top: 225px;
    margin: 0;
    font-family: "Titillium Web", sans-serif;
    font-weight: 400;
    font-size: 33px;
    line-height: 37px;
    color: var(--burnt-orange);
  }
  .contact {
    position: absolute;
    right: 103px;
    top: 455px;
    text-align: right;
    color: var(--ink-light);
    font-family: "Titillium Web", sans-serif;
  }
  .contact-name {
    margin: 0 0 14px;
    font-weight: 400;
    font-size: 49px;
    line-height: 1.1;
  }
  .contact-line {
    margin: 0;
    font-weight: 300;
    font-size: 41px;
    line-height: 47px;
  }
</style>
</head>
<body>
<main class="canvas">
  <svg class="card-art" viewBox="0 0 1110 685" preserveAspectRatio="none" aria-hidden="true">
    <defs>
      <clipPath id="card-shape">
        <rect x="24" y="35" width="1062" height="614" rx="40" ry="40"/>
      </clipPath>
    </defs>
    <rect x="24" y="35" width="1062" height="614" rx="40" ry="40" fill="var(--card)"/>
    <g clip-path="url(#card-shape)">
      <path class="wave-accent" transform="translate(0,-13)" fill="var(--burnt-orange)"
        d="M0 478 C 70 430, 150 405, 240 425 C 300 440, 340 470, 400 468 C 500 465, 580 330, 700 305 C 800 290, 880 315, 940 325 C 1010 335, 1030 250, 1050 210 C 1065 180, 1078 172, 1110 160 L1110 685 L0 685 Z"/>
      <path class="wave-field" fill="var(--olive)"
        d="M0 478 C 70 430, 150 405, 240 425 C 300 440, 340 470, 400 468 C 500 465, 580 330, 700 305 C 800 290, 880 315, 940 325 C 1010 335, 1030 250, 1050 210 C 1065 180, 1078 172, 1110 160 L1110 685 L0 685 Z"/>
    </g>
    <rect x="24" y="35" width="1062" height="614" rx="40" ry="40" fill="none" stroke="var(--card-edge)" stroke-width="1"/>
  </svg>

  <div class="brand-mark" aria-hidden="true"></div>
  <h1 class="brand-name">Bright-Moss Yards</h1>
  <p class="tagline">Your complete Gardening and<br>lawn maintenance, Horticultural care</p>

  <section class="contact">
    <p class="contact-name">Colin Breversted</p>
    <p class="contact-line">Phone: 0438159027</p>
    <p class="contact-line">Email: brightmossyards@mailbarn.net</p>
  </section>
</main>
</body>
</html>
```